Law firm Seeks Modern and Engaging Site Redesign

Law firm seeks a new web site. Should be modern, but retaining existing logo. Needs to include contact section, professional bio, services offered, and contact information.

The site should be modern, responsive, and able to be SEO optimized.

The finished product should be coded in a Wordpress site, which I will provide. I can work with other platforms, including Wix, but WP is preferred.

Note the current site is https://www.tallowfinchlaw.com/#/home

Target Market(s)

Family Law Practice

Industry/Entity Type

Legal

Coding

Coded - Design and coding required

Number of Pages Required

4 page

Font styles to use
Sans Serif

Requirements
Must have
• Service description
Bio pages for partners
Contact Form
Awards/Publication page

```html
<!DOCTYPE html>
<html lang="en">
<head>
<meta charset="utf-8">
<title>Tallow Finch — Family Law Practice</title>
<link href="https://fonts.googleapis.com/css2?family=Libre+Baskerville:wght@400;700&family=Montserrat:wght@400;500;600;700&display=swap" rel="stylesheet">
<style>
:root{
  --indigo:#414b8f;
  --indigo-dark:#333d7c;
  --heading:#2f3b7a;
  --accent:#4a6bd6;
  --accent-light:#6d86e0;
  --text:#555;
  --bronze:#9c8a6e;
  --white:#fff;
}
*{box-sizing:border-box;margin:0;padding:0}
html,body{width:1200px;height:3861px;overflow:hidden}
body{position:relative;font-family:"Montserrat",sans-serif;color:var(--text);background:var(--white)}
.abs{position:absolute}
.serif{font-family:"Libre Baskerville",serif;font-weight:400}
.rule{width:42px;height:3px;background:var(--indigo);}
.btn{position:absolute;display:flex;align-items:center;justify-content:center;border-radius:20px;background:var(--accent);color:#fff;font-size:12px;font-weight:600;letter-spacing:.5px}

/* top bar */
.topbar{left:0;top:0;width:1200px;height:33px;background:var(--indigo);color:#fff;font-size:11px;font-weight:500}
.topbar .item{position:absolute;top:6px;display:flex;align-items:center;gap:8px}
.topbar .ico{width:22px;height:22px;border-radius:50%;background:#fff;display:flex;align-items:center;justify-content:center}

/* nav */
.nav{left:0;top:33px;width:1200px;height:56px;background:#fff;border-bottom:1px solid #eee}
.brand{position:absolute;display:flex;align-items:center;gap:8px;font-size:20px;font-weight:500;color:var(--indigo);white-space:nowrap}
.brand .mark{width:12px;height:12px;background:var(--accent)}
.brand.light{color:#fff}
.brand.light .mark{background:#fff}
.menu{position:absolute;top:22px;left:0;width:1200px;height:20px;font-size:13px;color:#333}
.menu span{position:absolute;top:0;white-space:nowrap}
.menu .on{color:var(--accent)}

/* hero */
.hero{left:0;top:89px;width:1200px;height:532px;background:linear-gradient(120deg,#4a4a48 0%,#6c6a66 40%,#8a8680 70%,#5b5955 100%)}
.hero h1{position:absolute;top:178px;width:100%;text-align:center;color:#fff;font-size:48px}
.hero p{position:absolute;top:245px;left:370px;width:460px;text-align:center;color:#eee;font-size:15px;line-height:25px}
.notch{left:572px;top:595px;width:56px;height:30px}

/* about */
.about-frame{left:143px;top:698px;width:338px;height:384px;border:2px solid var(--accent)}
.about-photo{left:163px;top:712px;width:350px;height:381px;background:linear-gradient(160deg,#8a8f98,#4b5260 60%,#2f3440)}
.badge{left:312px;top:938px;width:238px;height:224px;background:#fff;border:6px solid var(--bronze)}
.badge-hatch{left:350px;top:970px;width:214px;height:208px;background:repeating-linear-gradient(45deg,#ccc 0 1px,transparent 1px 5px)}
.badge .t1{position:absolute;left:20px;top:28px;color:var(--accent);font-size:15px}
.badge .num{position:absolute;left:30px;top:46px;font-size:100px;font-weight:700;color:#111;letter-spacing:-4px;line-height:1}
.badge .t2{position:absolute;right:22px;top:160px;color:var(--accent);font-size:18px}
.badge .t3{position:absolute;left:30px;top:182px;color:var(--accent);font-size:20px;font-weight:600}
.about-h{left:619px;top:757px;font-size:38px;color:var(--heading)}
.about-text{left:619px;top:828px;width:440px;font-size:11px;line-height:22.5px;color:#555;text-align:justify}
.about-text p{margin-bottom:13px}

/* services */
.sec-h{width:1200px;left:0;text-align:center;color:var(--heading);font-size:36px}
.tab{position:absolute;top:1323px;height:38px;border-radius:20px;display:flex;align-items:center;justify-content:center;font-size:12px;font-weight:600;color:#fff}
.carousel{left:0;top:1391px;width:1200px;height:308px;display:flex}
.panel{width:240px;height:308px;position:relative;border-right:1px solid rgba(255,255,255,.25)}
.panel span{position:absolute;bottom:22px;width:100%;text-align:center;color:#fff;font-family:"Libre Baskerville",serif;font-size:15px}
.arrow{position:absolute;top:1530px;width:28px;height:28px;border-radius:50%;display:flex;align-items:center;justify-content:center}

/* team */
.card{position:absolute;top:1845px;width:200px;height:332px;border:1px solid #d9dbe2;background:#fff;box-shadow:0 0 0 6px #f6f6f8}
.card.active{border:2px solid var(--accent)}
.card .ph{position:absolute;left:6px;top:6px;right:6px;height:207px}
.card .name{position:absolute;top:238px;width:100%;text-align:center;font-size:13px;font-weight:700;color:#222}
.card.active .name{color:var(--accent)}
.card .role{position:absolute;top:258px;width:100%;text-align:center;font-size:12px;color:#666}
.card .soc{position:absolute;top:290px;width:100%;display:flex;justify-content:center;gap:12px}
.card .soc i{width:14px;height:14px;background:#5b6a8e;border-radius:3px}
.card .soc i:nth-child(2){background:var(--indigo)}

/* band */
.band{left:0;top:2251px;width:1200px;height:300px;background:linear-gradient(90deg,#6a84e0 0%,#5d7ad9 50%,#6a86e2 100%)}
.band h2{position:absolute;top:65px;width:100%;text-align:center;color:#fff;font-size:36px}
.band .rule{position:absolute;left:580px;top:115px;background:#fff}
.band p{position:absolute;top:133px;left:230px;width:740px;text-align:center;color:#fff;font-size:12.5px;font-weight:500;line-height:20px}
.call{position:absolute;left:417px;top:186px;width:366px;height:46px;border-radius:6px;background:#fff;display:flex;align-items:center;justify-content:center;gap:10px;font-size:16px;color:#222}

/* testimonial */
.t-photo{left:437px;top:2623px;width:623px;height:418px;background:linear-gradient(90deg,#e8edf3 0%,#c5d3e3 50%,#8796a8 75%,#dfe6ee 100%)}
.t-card{left:138px;top:2722px;width:600px;height:372px;background:#fff;box-shadow:0 4px 18px rgba(0,0,0,.12)}
.t-card h2{position:absolute;left:30px;top:58px;font-size:36px;color:var(--heading)}
.t-card .rule{position:absolute;left:30px;top:115px}
.t-card .quote{position:absolute;left:30px;top:140px;width:540px;font-size:11.5px;font-style:italic;line-height:21.5px;color:#444}
.t-card .who{position:absolute;left:30px;top:325px;font-size:15px;font-weight:600;color:var(--accent)}
.t-arrow{position:absolute;left:700px;width:38px;height:28px;background:var(--accent-light);display:flex;align-items:center;justify-content:center}

/* quote & footer */
.foot{left:0;top:3482px;width:1200px;height:356px;background:var(--indigo)}
.q-card{left:255px;top:3198px;width:690px;height:468px;background:#f7f7f8;border:1px solid #e2e2e6;border-radius:6px;box-shadow:0 2px 10px rgba(0,0,0,.15)}
.q-card h2{position:absolute;top:52px;width:100%;text-align:center;font-size:36px;color:var(--heading)}
.q-card .rule{position:absolute;left:324px;top:100px}
.field{position:absolute;background:#fff;border:1px solid #d5d5d9;font-size:12px;color:#666;padding:9px 10px}
.finfo{position:absolute;top:3722px;display:flex;align-items:center;gap:12px;color:#fff;font-size:11px;line-height:15px;font-weight:500}
.vsep{position:absolute;top:3718px;width:0;height:52px;border-left:1px dashed rgba(255,255,255,.6)}
.copy{left:0;top:3838px;width:1200px;height:23px;background:#4e67cf;color:#fff;font-size:11px;font-weight:500}
.copy .c{position:absolute;left:143px;top:5px}
.copy .soc{position:absolute;left:942px;top:2px;display:flex;gap:9px}
.copy .soc i{width:20px;height:20px;border-radius:50%;background:var(--indigo-dark)}
</style>
</head>
<body>

<!-- top bar -->
<div class="abs topbar">
  <div class="item" style="left:140px">
    <span class="ico"><svg width="12" height="12" viewBox="0 0 24 24"><path fill="#414b8f" d="M6.6 10.8a15 15 0 0 0 6.6 6.6l2.2-2.2c.3-.3.7-.4 1-.2 1.1.4 2.3.6 3.6.6.6 0 1 .4 1 1V20c0 .6-.4 1-1 1A17 17 0 0 1 3 4c0-.6.4-1 1-1h3.5c.6 0 1 .4 1 1 0 1.3.2 2.5.6 3.6.1.3 0 .7-.2 1z"/></svg></span>
    PHONE: (555) 014-2290
  </div>
  <div class="item" style="left:834px">
    <span class="ico"><svg width="12" height="10" viewBox="0 0 24 18"><rect x="1" y="1" width="22" height="16" rx="2" fill="#414b8f"/><path d="M2 2l10 8 10-8" stroke="#fff" stroke-width="2" fill="none"/></svg></span>
    EMAIL: info@tallowfinch.com
  </div>
</div>

<!-- nav -->
<div class="abs nav">
  <div class="brand" style="left:140px;top:16px"><span class="mark"></span>Tallow Finch</div>
  <div class="menu">
    <span class="on" style="left:474px">Home</span>
    <span style="left:560px">Family Law</span>
    <span style="left:684px">Criminal Law</span>
    <span style="left:817px">About Us</span>
    <span style="left:928px">Blog</span>
    <span style="left:1005px">Contact</span>
  </div>
</div>

<!-- hero -->
<div class="abs hero" role="img" aria-label="Photo of an attorney's hand resting on a desk beside a gavel, pen and legal documents">
  <h1 class="serif">Family Law Practice</h1>
  <p>30+ years of experience assisting clients with all of their family law and criminal law needs</p>
  <div class="btn" style="left:545px;top:315px;width:110px;height:30px;background:var(--indigo);font-size:11px">CONTACT US</div>
</div>
<svg class="abs notch" viewBox="0 0 56 30"><path d="M0 30 C14 30 14 8 28 8 C42 8 42 30 56 30Z" fill="#fff"/><rect x="22" y="10" width="12" height="20" rx="6" fill="none" stroke="#444" stroke-width="1.4"/><path d="M25 17l3 3 3-3M25 21l3 3 3-3" stroke="#444" stroke-width="1.2" fill="none"/></svg>

<!-- about -->
<div class="abs about-frame"></div>
<div class="abs about-photo" role="img" aria-label="Portrait of a senior partner seated in an office"></div>
<div class="abs badge-hatch"></div>
<div class="abs badge">
  <span class="t1">Have Over</span>
  <span class="num">30</span>
  <span class="t2">+ Years</span>
  <span class="t3">Experience</span>
</div>
<h2 class="abs serif about-h">About Us</h2>
<div class="abs rule" style="left:619px;top:812px"></div>
<div class="abs about-text">
  <p>The law firm of Tallow Finch, LLC is based in Alder County, conveniently located in Larkfield, New Jersey in 48 Meridian Plaza. We serve the needs of clients throughout Alder County, as well as, clients from several other counties, including, but not limited to, Wexford, Marlow, Essenby and Hollis. Between our partners, we have over 30+ years of experience assisting clients with all of their family law and criminal law needs.</p>
  <p>Often times the areas of family law and criminal law cross paths, which can be both emotionally and financially complex. We understand that our client's case is unique and pride ourselves on being responsive to all of our clients needs.</p>
</div>
<div class="btn" style="left:619px;top:1075px;width:114px;height:35px;font-weight:500;font-size:11px">READ MORE</div>

<!-- services -->
<h2 class="abs serif sec-h" style="top:1240px">Our Law Services</h2>
<div class="abs rule" style="left:579px;top:1291px"></div>
<div class="tab" style="left:459px;width:136px;background:var(--indigo)">FAMILY LAW</div>
<div class="tab" style="left:607px;width:136px;background:var(--accent)">CRIMINAL LAW</div>
<div class="abs carousel">
  <div class="panel" role="img" aria-label="Photo of a hand gesturing beside a gavel" style="background:linear-gradient(180deg,#a0764e,#6b4a30 60%,#2a211a)"><span>Divorce</span></div>
  <div class="panel" role="img" aria-label="Photo of a young child holding a plush toy" style="background:linear-gradient(180deg,#8b8f93,#5c6066 60%,#2b2d31)"><span>Child Custody</span></div>
  <div class="panel" role="img" aria-label="Photo of a child support agreement document with eyeglasses" style="background:linear-gradient(180deg,#e4c9a0,#b58b55 60%,#3f3123)"><span>Child Support</span></div>
  <div class="panel" role="img" aria-label="Photo of a gavel resting on a paper about alimony" style="background:linear-gradient(180deg,#b7894f,#7d6548 60%,#2e271f)"><span>Alimony</span></div>
  <div class="panel" role="img" aria-label="Photo of a distressed child seated on the floor at home" style="background:linear-gradient(180deg,#c2b4a4,#857463 60%,#2f2923)"><span>Domestic violence</span></div>
</div>
<div class="arrow" style="left:14px;background:#fff"><svg width="10" height="10" viewBox="0 0 10 10"><path d="M6.5 2L3.5 5l3 3" stroke="#333" stroke-width="1.5" fill="none"/></svg></div>
<div class="arrow" style="left:1144px;background:var(--accent)"><svg width="10" height="10" viewBox="0 0 10 10"><path d="M3.5 2l3 3-3 3" stroke="#fff" stroke-width="1.5" fill="none"/></svg></div>

<!-- team -->
<h2 class="abs serif sec-h" style="top:1765px">Our Team</h2>
<div class="abs rule" style="left:579px;top:1816px"></div>
<div class="card" style="left:148px">
  <div class="ph" role="img" aria-label="Portrait of Daniel R. Tallow in an office" style="background:linear-gradient(160deg,#9aa0a8,#4b5260)"></div>
  <div class="name">Daniel R. Tallow</div><div class="role">Partner, Attorney</div>
  <div class="soc"><i></i><i></i><i></i><i></i></div>
</div>
<div class="card active" style="left:383px">
  <div class="ph" role="img" aria-label="Portrait of Marcus T. Finch at his desk" style="background:linear-gradient(160deg,#a99a86,#4a4640)"></div>
  <div class="name">Marcus T. Finch</div><div class="role">Partner, Attorney</div>
  <div class="soc"><i></i><i></i><i></i><i></i></div>
</div>
<div class="card" style="left:618px">
  <div class="ph" role="img" aria-label="Portrait of Nora L. Hale outdoors" style="background:linear-gradient(160deg,#b08070,#6b5550)"></div>
  <div class="name">Nora L. Hale</div><div class="role">Associate Attorney</div>
  <div class="soc"><i></i><i></i><i></i><i></i></div>
</div>
<div class="card" style="left:853px">
  <div class="ph" role="img" aria-label="Portrait of Lena M. Carraway on a white background" style="background:linear-gradient(180deg,#f4f4f6,#c8cdd8 60%,#3f5fb0)"></div>
  <div class="name">Lena M. Carraway</div><div class="role">Associate Attorney</div>
  <div class="soc"><i></i><i></i><i></i><i></i></div>
</div>

<!-- band -->
<div class="abs band" role="img" aria-label="Blue tinted photo of a gavel and clasped hands">
  <h2 class="serif">Tallow Finch Legal Law</h2>
  <div class="rule"></div>
  <p>TO DISCUSS YOUR MATTER WITH EITHER MR. TALLOW OR MR. FINCH SEND US YOUR DETAILS ABOUT YOUR SITUATION OR CONTACT US DIRECTLY AT</p>
  <div class="call">
    <svg width="22" height="22" viewBox="0 0 24 24"><circle cx="12" cy="12" r="10.5" fill="none" stroke="#4a6bd6" stroke-width="1.4"/><path fill="#4a6bd6" d="M9 7.5c-.6.5-1 1.4-.8 2.6.4 2.4 2 4.6 4 5.8 1 .6 2 .6 2.6.2l.6-.6-1.6-1.6-.9.6c-1-.6-1.8-1.6-2.2-2.7l.6-.9L9.6 7z"/></svg>
    <b>CALL NOW -</b><span>(555) 014-2290.</span>
  </div>
</div>

<!-- testimonial -->
<div class="abs t-photo" role="img" aria-label="Photo of a smiling man in a grey suit and glasses"></div>
<div class="abs t-card">
  <h2 class="serif">What Our Clients Say?</h2>
  <div class="rule"></div>
  <div class="quote">Lorem ipsum dolor sit amet, consectetuer adipiscing elit, sed diam nonummy nibh euismod tincidunt ut laoreet dolore magna aliquam erat volutpat. Ut wisi enim ad minim veniam, quis nostrud exerci tation ullamcorper suscipit lobortis nisl ut aliquip ex ea commodo consequat. Duis autem vel eum iriure dolor in hendrerit in vulputate velit esse molestie consequat, vel illum dolore eu feugiat nulla facilisis at vero eros et accumsan et iusto odio dignissim qui blandit praesent luptatum zzril delenit augue duis dolore te feugait nulla facilisi.</div>
  <div class="who">–Sam Everly</div>
</div>
<div class="t-arrow" style="top:3034px;background:var(--indigo)"><svg width="18" height="10" viewBox="0 0 18 10"><path d="M1 5h15M12 1l4 4-4 4" stroke="#fff" stroke-width="1.4" fill="none"/></svg></div>
<div class="t-arrow" style="top:3064px"><svg width="18" height="10" viewBox="0 0 18 10"><path d="M17 5H2M6 1L2 5l4 4" stroke="#fff" stroke-width="1.4" fill="none"/></svg></div>

<!-- footer band -->
<div class="abs foot"></div>

<!-- quote form -->
<div class="abs q-card">
  <h2 class="serif">Request A Quote</h2>
  <div class="rule"></div>
  <div class="field" style="left:41px;top:113px;width:298px;height:30px">First Name</div>
  <div class="field" style="left:351px;top:113px;width:298px;height:30px">Last Name</div>
  <div class="field" style="left:41px;top:156px;width:298px;height:30px">Phone</div>
  <div class="field" style="left:351px;top:156px;width:298px;height:30px">Email</div>
  <div class="field" style="left:41px;top:205px;width:608px;height:32px">Practice Area
    <svg style="position:absolute;right:12px;top:11px" width="12" height="8" viewBox="0 0 12 8"><path d="M1 1l5 5 5-5" stroke="#222" stroke-width="1.8" fill="none"/></svg></div>
  <div class="field" style="left:41px;top:255px;width:608px;height:106px">Message</div>
  <div class="btn" style="left:288px;top:401px;width:113px;height:35px;font-weight:500">Send Request</div>
</div>

<!-- footer info -->
<div class="brand light" style="left:140px;top:3734px"><span class="mark"></span>Tallow Finch</div>
<div class="vsep" style="left:340px"></div>
<div class="finfo" style="left:360px">
  <svg width="40" height="40" viewBox="0 0 40 40" fill="none" stroke="#fff" stroke-width="1.4"><path d="M4 20L20 6l16 14"/><path d="M9 16v20h22V16"/><path d="M17 36V25h6v11"/></svg>
  <span>Tallow &amp; Finch LLC<br>48 Meridian Plaza Drive Suite<br>210 Larkfield, NJ 07990</span>
</div>
<div class="vsep" style="left:597px"></div>
<div class="finfo" style="left:614px">
  <svg width="22" height="40" viewBox="0 0 22 40" fill="none" stroke="#fff" stroke-width="1.4"><rect x="2" y="2" width="18" height="36" rx="3"/><path d="M2 8h18M2 31h18"/><circle cx="11" cy="34.5" r="1.3"/></svg>
  <span>Contact:- (555) 014-2290<br>Fax:- (555) 014-2291</span>
</div>
<div class="vsep" style="left:805px"></div>
<div class="finfo" style="left:824px">
  <svg width="36" height="26" viewBox="0 0 36 26" fill="none" stroke="#fff" stroke-width="1.4"><rect x="1" y="1" width="34" height="24"/><path d="M1 1l17 13L35 1M1 25l12-11M35 25L23 14"/></svg>
  <span style="font-weight:400">Email : info@tallowfinch.com<br>Send us your query anytime!</span>
</div>

<div class="abs copy">
  <span class="c">Copyright &nbsp;2020. Tallowfinch Legal Law. All Rights Reserved.</span>
  <div class="soc"><i></i><i></i><i></i><i></i></div>
</div>

</body>
</html>
```